PROFESSIONAL MODERN REDESIGN OF CURRENT WEBSITE USING ALL SAME CONTENT

I need to redesign existing website using all existing exact content. Please do not leave anything missing. Use all content.

www.brightpathpromotionsgroup.biz

Target Market(s)

Small business owners, business to business, B2B

Industry/Entity Type

Direct Marketing

Number of Pages Required

5+ page

Colors

Designer to choose colors to be used in the design.

Requirements
Must have
• Must use exact same content as www.brightpathpromotionsgroup.biz
Nice to have
• I'd like this to be an easy to read professionally designed website with all modern elements...
Should not have
• Open

```html
<!DOCTYPE html>
<html lang="en">
<head>
<meta charset="utf-8">
<title>Contact – Brightpath Promotions</title>
<link rel="stylesheet" href="https://fonts.googleapis.com/css2?family=Montserrat:wght@400;500;600;700&display=swap">
<style>
:root{
  --ink-dark:#15212c;
  --footer-bg:#253a50;
  --accent:#0a97df;
  --accent-btn:#0699f2;
  --brand-blue:#1f6fb8;
  --panel:#edeef2;
  --field-border:#7f9ab6;
  --label:#27384a;
  --nav-text:#3f4852;
  --white:#ffffff;
}
*{box-sizing:border-box;margin:0;padding:0}
html,body{width:1200px;height:2385px;overflow:hidden}
body{position:relative;background:var(--white);font-family:'Montserrat',sans-serif;color:var(--label)}
.topbar{position:absolute;left:0;top:0;width:1200px;height:29px;background:var(--ink-dark);color:var(--white);font-size:10.5px;font-weight:500}
.topbar .phones{position:absolute;left:122px;top:8px}
.topbar .account{position:absolute;right:108px;top:8px;font-weight:700;letter-spacing:1px}
.brand{position:absolute;left:0;width:1200px;top:48px;text-align:center;font-size:20px;font-weight:700;color:var(--brand-blue);letter-spacing:1px}
.brand .mark{display:inline-block;width:14px;height:14px;background:var(--brand-blue);margin-right:8px;vertical-align:1px}
.mainnav{position:absolute;left:0;width:1200px;top:113px;display:flex;justify-content:center;gap:31px;font-size:10.5px;font-weight:500;color:var(--nav-text)}
.mainnav .current{color:var(--accent)}
.hero{position:absolute;left:0;top:145px;width:1200px;height:255px;background:linear-gradient(100deg,#3d74b3 0%,#2f64a6 40%,#173c6e 48%,#3a73b5 60%,#5a90c9 80%,#1e4677 100%)}
.hero h1{position:absolute;left:0;width:1200px;top:100px;text-align:center;font-size:47px;font-weight:400;color:var(--white);letter-spacing:3px;line-height:1}
.intro{position:absolute;left:0;width:1200px;top:465px;text-align:center;font-size:23px;font-weight:600;color:var(--accent)}
.form-panel{position:absolute;left:155px;top:558px;width:883px;height:1069px;background:var(--panel)}
.field-label{position:absolute;left:274px;font-size:18.5px;font-weight:600;letter-spacing:1.2px;color:var(--label)}
.field{position:absolute;left:273px;width:654px;height:61px;background:var(--white);border:1px solid var(--field-border);border-radius:3px}
.field.message{height:235px}
.submit{position:absolute;left:273px;top:1460px;width:654px;height:62px;background:var(--accent-btn);color:var(--white);font-size:18.5px;font-weight:600;letter-spacing:2px;display:flex;align-items:center;justify-content:center;border-radius:2px}
.footer{position:absolute;left:0;top:1717px;width:1200px;height:589px;background:var(--footer-bg);color:var(--white);font-size:11.5px;font-weight:600}
.footer h3{position:absolute;font-size:13px;font-weight:500;letter-spacing:3.5px;color:var(--accent)}
.footer .logo{position:absolute;left:230px;top:68px;font-size:34px;font-weight:700;color:var(--brand-blue);letter-spacing:1px}
.footer .col{position:absolute}
.footer .col p{line-height:20.8px}
.quicklinks a,.social a{display:block;color:var(--white);text-decoration:none}
.quicklinks a{height:28.7px}
.social a{height:31.8px}
.copyright{position:absolute;left:0;top:2306px;width:1200px;height:79px;background:var(--ink-dark);color:#3a86c8;font-size:11px;text-align:center;padding-top:32px}
</style>
</head>
<body>
<header class="topbar">
  <div class="phones">USA Office : 555-014-2290 &nbsp;|&nbsp; International : 1-800-555-0147</div>
  <div class="account">LOGIN &nbsp;&nbsp;|&nbsp;&nbsp; SIGNUP</div>
</header>
<div class="brand"><span class="mark"></span>BRIGHTPATH PROMOTIONS</div>
<nav class="mainnav">
  <span>HOME</span><span>OUR INCENTIVES</span><span>SAMPLES</span><span>AFFILIATES</span><span>TESTIMONIALS</span><span>FAQ</span><span class="current">CONTACT</span>
</nav>
<section class="hero" role="img" aria-label="Photo of blue glass office building facades">
  <h1>CONTACT</h1>
</section>
<p class="intro">Fill out this contact form and a BPPG Representative will get back to you shortly.</p>
<div class="form-panel"></div>
<label class="field-label" style="top:626px">First Name*</label>
<div class="field" style="top:661px"></div>
<label class="field-label" style="top:759px">Last Name*</label>
<div class="field" style="top:792px"></div>
<label class="field-label" style="top:892px">Email</label>
<div class="field" style="top:924px"></div>
<label class="field-label" style="top:1025px">Phone #</label>
<div class="field" style="top:1058px"></div>
<label class="field-label" style="top:1153px">Message*</label>
<div class="field message" style="top:1186px"></div>
<div class="submit">CONTACT NOW</div>
<footer class="footer">
  <div class="logo">BPP</div>
  <h3 style="left:230px;top:140px">CONTACT DETAILS</h3>
  <div class="col" style="left:230px;top:171px">
    <p>Brightpath Promotions Group,<br>Inc.<br>418 Harborline Drive<br>Bayview CA 90001</p>
  </div>
  <h3 style="left:230px;top:279px">HOURS</h3>
  <div class="col" style="left:230px;top:310px">
    <p>Monday - Friday: 8:00AM - 5:00PM PST-<br>Saturday - Sunday: CLOSED</p>
  </div>
  <h3 style="left:555px;top:68px">QUICKLINKS</h3>
  <div class="col quicklinks" style="left:555px;top:103px">
    <a>Home</a><a>Our Incentives</a><a>Samples</a><a>Affiliate</a><a>Testimonials</a><a>FAQ</a><a>Contact Us</a><a>Terms &amp; Conditions</a><a>Privacy Policy</a><a>Hoteliers</a><a>BPP PDF Flyer</a><a>BPP PDF Brochure</a><a>BPP Certificates List</a><a>How To Use BPP Certificates</a><a>Free Viseo Ad Mock Up for Marketing</a>
  </div>
  <h3 style="left:858px;top:68px">SOCIAL</h3>
  <div class="col social" style="left:858px;top:103px">
    <a>Community Page</a><a>Video Channel</a><a>Business Network</a><a>Photo Stream</a>
  </div>
</footer>
<div class="copyright">Copyright 2005-2020 Brightpath Promotions Group, Inc. All Rights Reserved.</div>
</body>
</html>
```